Modern Spot UV Business Card design

We are a relatively new real estate agency. We need a business card that reflects the professionalism and prestige of our company but is also modern and fresh, based around our logo.
We would love to utilise spot UV.
Happy to let the designers use their imagination and see what they come up with (we're not very creative, so have no ideas for you, sorry) :-)
We'd like one for each staff member, but I've just provided one staff members photo here to avoid confusion.

Target Market(s)

Families

Industry/Entity Type

Real Estate Agent

Contact Information for Business Card

Colin Varga - Director & Principal
Mobile: 0491 527 806
Email: colin.varga@vbrokers.example.com.au
Phone: (08) 7364 9150
Fax: (08) 7364 9182
www.vargabrokersrealestate.example.com.au

Font styles to use
Other font styles liked:
• Kabel Dm BT

Requirements
Must have
• Contact details, logo, photo, spot UV
Nice to have
• Modern interesting features that will make people comment. Nothing too feminine nor too masculine.
Should not have
• No houses! Nothing typical of a real estate agent.

```html
<!DOCTYPE html>
<html lang="en">
<head>
<meta charset="utf-8">
<title>Varga Brokers – Business Card</title>
<link rel="stylesheet" href="https://fonts.googleapis.com/css2?family=Jost:wght@500;600;700&display=swap">
<style>
  :root {
    --backdrop: #a8a8a8;
    --card-white: #ffffff;
    --charcoal: #3c3c3e;
    --charcoal-light: #4a4a4d;
    --brand-blue: #1ca6e6;
    --brand-blue-deep: #1682bd;
    --ink: #1f1f21;
    --photo-light: #eef0f2;
    --photo-dark: #43464b;
  }
  * { box-sizing: border-box; margin: 0; padding: 0; }
  html, body {
    width: 1200px; height: 900px; overflow: hidden;
    background: var(--backdrop);
    font-family: "Jost", sans-serif;
  }
  .canvas { position: relative; width: 1200px; height: 900px; }

  .card {
    position: absolute;
    width: 620px; height: 350px;
    background: var(--card-white);
    box-shadow: 0 6px 18px rgba(0,0,0,.28);
    overflow: hidden;
  }
  .card--front { left: 290px; top: 60px; }
  .card--back  { left: 290px; top: 480px; }

  .card__bands { position: absolute; inset: 0; }
  .portrait {
    position: absolute; left: 0; top: 22px;
    width: 290px; height: 180px;
    background: linear-gradient(180deg, var(--photo-light) 0%, #c9ccd0 45%, var(--photo-dark) 100%);
  }

  .brand {
    position: absolute;
    display: flex; align-items: center;
    font-weight: 700; color: var(--ink); line-height: 1; white-space: nowrap;
  }
  .brand__dot { border-radius: 50%; background: var(--brand-blue); flex: none; }
  .brand--front { right: 40px; top: 68px; font-size: 34px; gap: 12px; }
  .brand--front .brand__dot { width: 16px; height: 16px; }
  .brand--back { left: 50%; top: 50%; transform: translate(-50%, -50%); font-size: 60px; gap: 20px; }
  .brand--back .brand__dot { width: 28px; height: 28px; }

  .agent {
    position: absolute; left: 36px; top: 208px; color: var(--card-white);
  }
  .agent__name { font-size: 20px; font-weight: 600; letter-spacing: 1px; text-transform: uppercase; }
  .agent__role { font-size: 15px; font-weight: 500; margin-top: 2px; }

  .phones {
    position: absolute; right: 34px; top: 216px;
    list-style: none; color: var(--card-white);
  }
  .phones li {
    display: flex; justify-content: flex-end; align-items: center; gap: 10px;
    font-size: 14px; font-weight: 500; letter-spacing: .5px; height: 21px;
  }
  .online {
    position: absolute; left: 36px; top: 282px;
    list-style: none; color: var(--card-white);
  }
  .online li {
    display: flex; align-items: center; gap: 12px;
    font-size: 15.5px; font-weight: 500; height: 26px;
  }
  .icon { width: 16px; height: 16px; flex: none; }
</style>
</head>
<body>
<main class="canvas">

  <section class="card card--front" aria-label="Business card front">
    <svg class="card__bands" width="620" height="350" viewBox="0 0 620 350" aria-hidden="true">
      <rect x="0" y="195" width="620" height="155" fill="var(--charcoal)"/>
      <polygon points="380,190 620,182 620,195 380,195" fill="var(--brand-blue)"/>
      <polygon points="430,195 620,195 620,205 440,205" fill="var(--charcoal-light)"/>
      <polygon points="0,200 330,200 400,264 0,264" fill="var(--brand-blue)"/>
      <polygon points="330,200 440,196 400,236" fill="var(--brand-blue-deep)"/>
    </svg>

    <div class="portrait" role="img" aria-label="Portrait photo of Colin Varga in a dark suit"></div>

    <div class="brand brand--front">
      <span class="brand__dot" aria-hidden="true"></span>
      <span class="brand__name">Varga Brokers</span>
    </div>

    <div class="agent">
      <div class="agent__name">Colin Varga</div>
      <div class="agent__role">Director &amp; Principal</div>
    </div>

    <ul class="phones">
      <li>0491 527 806
        <svg class="icon" viewBox="0 0 16 16" aria-label="Mobile"><rect x="4" y="1" width="8" height="14" rx="1.5" fill="none" stroke="var(--brand-blue)" stroke-width="1.5"/><circle cx="8" cy="12.5" r="0.9" fill="var(--brand-blue)"/></svg>
      </li>
      <li>(08) 7364 9150
        <svg class="icon" viewBox="0 0 16 16" aria-label="Phone"><path d="M3.5 1.5l2.5 3-1.5 1.5c.8 2 2.5 3.7 4.5 4.5L10.5 9l3 2.5-1.5 2.5C7 14 2 9 1.5 3z" fill="var(--brand-blue)"/></svg>
      </li>
      <li>(08) 7364 9182
        <svg class="icon" viewBox="0 0 16 16" aria-label="Fax"><rect x="4" y="1.5" width="8" height="4" fill="var(--brand-blue)"/><rect x="1.5" y="6" width="13" height="6" rx="1" fill="var(--brand-blue)"/><rect x="4" y="10" width="8" height="4.5" fill="var(--card-white)" stroke="var(--brand-blue)" stroke-width="1"/></svg>
      </li>
    </ul>

    <ul class="online">
      <li>
        <svg class="icon" viewBox="0 0 16 16" aria-label="Email"><circle cx="8" cy="8" r="8" fill="var(--brand-blue)"/><rect x="3.5" y="5" width="9" height="6.5" fill="none" stroke="var(--charcoal)" stroke-width="1.2"/><path d="M3.5 5l4.5 3.5L12.5 5" fill="none" stroke="var(--charcoal)" stroke-width="1.2"/></svg>
        colin.varga@vbrokers.example.com.au
      </li>
      <li>
        <svg class="icon" viewBox="0 0 16 16" aria-label="Website"><circle cx="8" cy="8" r="8" fill="var(--brand-blue)"/><ellipse cx="8" cy="8" rx="3" ry="6" fill="none" stroke="var(--charcoal)" stroke-width="1"/><path d="M2 8h12" stroke="var(--charcoal)" stroke-width="1"/></svg>
        www.vargabrokersrealestate.example.com.au
      </li>
    </ul>
  </section>

  <section class="card card--back" aria-label="Business card back">
    <div class="brand brand--back">
      <span class="brand__dot" aria-hidden="true"></span>
      <span class="brand__name">Varga Brokers</span>
    </div>
  </section>

</main>
</body>
</html>
```